Velmor Integrated Company Profile

We are looking for a new design for our company profile. We need two output formats. A PDF version to use as a soft copy. Another version is needed for printing.

We are seeking an A4 profile based on the same text content of our old one. Some new content will be provided once the graphics are confirmed.

Attached is our old profile. Please give us a newer design. Once design is confirmed we will provide the new content to use.
I am available for any answers or feedback.

Target Market(s)

This is used for introducing our company to the customers.
We are also seeking investors, so they might be considered

Industry/Entity Type

Information Technology

Requirements
Must have
• Info-graphics based on the data in old profile
• Some info-graphics about number of orders, customers and sales volume
• We have two websites for selling online; nilecallkit.com and dunelinkgear.com. We need to include them in a way or another in the profile. Their logos are in the attached files.
Nice to have
• Any new suggestions about content to include in the profile will be welcomed

```html
<!DOCTYPE html>
<html lang="en">
<head>
<meta charset="utf-8">
<title>Velmor Integrated – Company Profile</title>
<link href="https://fonts.googleapis.com/css2?family=Questrial&display=swap" rel="stylesheet">
<style>
  :root{
    --brand-blue:#1f4e8f;
    --brand-blue-dark:#173d72;
    --brand-orange:#e08a1e;
    --ink:#555a60;
    --ink-soft:#7a7f86;
    --paper:#f4f4f4;
    --page-bg:#e4e4e4;
    --rule:#cfd3d8;
  }
  *{box-sizing:border-box;margin:0;padding:0}
  html,body{width:1200px;height:880px;overflow:hidden}
  body{background:var(--page-bg);font-family:"Questrial",sans-serif;color:var(--ink);position:relative}

  .spread{position:absolute;left:40px;width:1120px;display:flex;box-shadow:0 4px 14px rgba(0,0,0,.18)}
  .spread--inside{top:24px;height:400px}
  .spread--outside{top:452px;height:404px}
  .page{position:relative;width:560px;height:100%;overflow:hidden;background:var(--paper)}

  /* inside bands */
  .band-top{position:absolute;top:0;left:0;right:0;height:22px;background:var(--brand-blue)}
  .band-bottom{position:absolute;bottom:0;left:0;right:0;height:14px;background:var(--brand-orange)}

  /* left inside page */
  .pillars{position:absolute;top:40px;left:22px;right:22px;display:flex;gap:16px}
  .pillar{flex:1}
  .pillar__photo{height:74px;background:linear-gradient(135deg,#8d97a3,#3f5f88)}
  .pillar__photo--values{background:linear-gradient(135deg,#c9ccd1,#5d6b7d)}
  .pillar__photo--principles{background:linear-gradient(135deg,#2f6fb3,#1b3f70)}
  .pillar__label{background:var(--brand-blue);color:#fff;font-size:12px;text-align:center;padding:5px 0;letter-spacing:.5px}
  .pillar__body{padding:16px 4px 0;font-size:9px;line-height:1.35}
  .pillar__body h3{color:var(--brand-blue);font-weight:400;font-size:11px;margin-top:8px}
  .pillar__body h3:first-child{margin-top:0}
  .pillar__body p{margin:1px 0}
  .bullets{list-style:none}
  .bullets li{position:relative;padding-left:11px;margin-bottom:6px}
  .bullets li::before{content:"";position:absolute;left:0;top:3px;width:5px;height:5px;background:var(--brand-blue)}

  /* right inside page */
  .services-title{position:absolute;top:40px;left:280px;width:260px;text-align:center;color:var(--brand-blue);font-size:14px;letter-spacing:.5px}
  .intro{position:absolute;top:42px;left:22px;width:230px;font-size:8.5px;line-height:1.35}
  .intro h4{color:var(--brand-blue);font-weight:400;font-size:11px;margin:10px 0 4px}
  .intro ul{list-style:none}
  .intro li{margin-bottom:5px}
  .service{position:absolute;top:72px;width:125px;text-align:center;font-size:8px;line-height:1.3}
  .service--collab{left:270px}
  .service--infra{left:410px}
  .service svg{display:block;margin:0 auto 4px}
  .service h5{color:var(--brand-blue);font-weight:400;font-size:9.5px;margin-bottom:3px}
  .partners{position:absolute;left:262px;top:222px;width:276px;height:150px;display:grid;grid-template-columns:repeat(4,1fr);grid-template-rows:repeat(3,1fr);border-top:1px solid var(--rule);border-left:1px solid var(--rule)}
  .partner{border-right:1px solid var(--rule);border-bottom:1px solid var(--rule);display:flex;align-items:center;justify-content:center}
  .partner--wide{grid-column:span 2}

  /* back cover */
  .back{background:var(--brand-blue)}
  .back__map{position:absolute;inset:0;background:radial-gradient(ellipse at 55% 55%,rgba(255,255,255,.10),rgba(255,255,255,0) 65%)}
  .back__name{position:absolute;top:40px;left:40px;color:#fff;font-size:22px;letter-spacing:3px;display:flex;align-items:center;gap:10px}
  .back__name span.mark{width:14px;height:14px;background:#fff}
  .back__sub{position:absolute;top:70px;left:64px;color:#d8e2f0;font-size:8px;letter-spacing:3px}
  .contact{position:absolute;left:40px;font-size:8.5px;line-height:1.45;color:#e6ecf5}
  .contact--eg{top:104px}
  .contact--ksa{top:190px}
  .contact h6{color:var(--brand-orange);font-weight:400;font-size:9px;letter-spacing:.5px}
  .contact b{font-weight:400;color:#fff}
  .shops{position:absolute;left:300px;top:130px}
  .shop{margin-bottom:28px}
  .shop__name{display:flex;align-items:center;gap:7px;color:var(--brand-orange);font-size:20px}
  .shop__name i{width:10px;height:10px;background:var(--brand-orange)}
  .shop__url{color:#d8e2f0;font-size:8.5px;margin-left:17px}

  /* front cover */
  .front{background:#fbfbfb}
  .front__photos{position:absolute;top:0;right:0;width:400px;height:230px;display:flex}
  .photo-servers{flex:1.1;background:linear-gradient(160deg,#c7cdd4,#5e6a78 70%,#2c3e5c)}
  .photo-phone{flex:1;background:linear-gradient(160deg,#b9d6d8,#6f8f96 60%,#333a40)}
  .front__url{position:absolute;top:246px;right:36px;color:var(--brand-blue);font-size:13px;letter-spacing:1px}
  .front__brand{position:absolute;top:240px;left:36px}
  .front__name{display:flex;align-items:center;gap:10px;color:var(--brand-orange);font-size:34px;letter-spacing:4px}
  .front__name i{width:18px;height:18px;background:var(--brand-blue)}
  .front__tagline-sub{color:var(--brand-blue);font-size:10px;letter-spacing:4px;margin:4px 0 0 28px}
  .front__claim{position:absolute;right:36px;bottom:40px;text-align:right}
  .front__claim .lead{color:var(--brand-orange);font-size:18px}
  .front__claim .main{color:var(--brand-blue);font-size:20px;letter-spacing:2px}
</style>
</head>
<body>

<!-- Inside spread -->
<section class="spread spread--inside">
  <article class="page page--about">
    <div class="band-top"></div>
    <div class="pillars">
      <div class="pillar">
        <div class="pillar__photo" role="img" aria-label="Photo of a hand touching a digital interface"></div>
        <div class="pillar__label">OUR STRATEGY</div>
        <div class="pillar__body">
          <h3>Assess &amp; Design:</h3>
          <p>· Upgrades and Fixes Communication</p>
          <p>· Client's Objective</p>
          <p>· Solution Design &amp; TCO Analysis</p>
          <h3>Implement:</h3>
          <p>· Project Plan &amp; Management</p>
          <p>· Certified Technical Team</p>
          <p>· Quality Assurance</p>
          <p>· Documentation &amp; Training</p>
          <h3>Follow Up:</h3>
          <p>· ROI &amp; Adoption Assurance</p>
          <p>· Budget Flexible Service Plans</p>
          <p>· Upgrades and Fixes Communication</p>
        </div>
      </div>
      <div class="pillar">
        <div class="pillar__photo pillar__photo--values" role="img" aria-label="Photo of a business handshake"></div>
        <div class="pillar__label">OUR VALUES</div>
        <div class="pillar__body">
          <h3>Commitment:</h3>
          <p>For those who are committed, a promise is responsibility, and this is how we guarantee a superior service</p>
          <h3>Expediency:</h3>
          <p>Accurately and professionally providing the most suitable solutions for your needs and perfectly apply it</p>
          <h3>Ingenuity:</h3>
          <p>Innovating creative techniques for our services and products</p>
        </div>
      </div>
      <div class="pillar">
        <div class="pillar__photo pillar__photo--principles" role="img" aria-label="Photo of a businessman with blue gear graphics"></div>
        <div class="pillar__label">OPERATING PRINCIPLES</div>
        <div class="pillar__body">
          <ul class="bullets">
            <li>Providing top of the line ICT consultancy services ensuring efficient work flow.</li>
            <li>Providing constant training for staff and associates to ensure state of the art solutions</li>
            <li>High standard of work ethics</li>
            <li>Ensuring value for money for our clients</li>
            <li>Creating action oriented management environment towards the ease of transactions</li>
          </ul>
        </div>
      </div>
    </div>
    <div class="band-bottom"></div>
  </article>

  <article class="page page--services">
    <div class="band-top"></div>
    <div class="intro">
      <p>Morbi accumsan ipsum velit. Nam nec tellus a odio tincidunt auctor a ornare odio. Sed non mauris vitae erat consequat auctor eu in elit. Class aptent taciti sociosqu ad litora torquent per conubia nostra, per inceptos himenaeos. Mauris in erat justo. Nullam ac urna eu felis dapibus condimentum sit amet a augue. Sed non neque elit. Sed ut imperdiet nisi. Proin condimentum fermentum nunc. Etiam pharetra, erat sed fermentum feugiat, velit mauris egestas quam, ut aliquam massa nisl quis neque. Suspendisse in orci enim.</p>
      <h4>You Get The Best Of...</h4>
      <ul>
        <li>- Morbi accumsan ipsum velit. Nam nec tellus a odio tincidunt auctor a ornare odio.</li>
        <li>- Morbi accumsan ipsum velit. Nam nec tellus a odio tincidunt auctor a ornare odio.</li>
        <li>- Morbi accumsan ipsum velit. Nam nec tellus a odio tincidunt auctor a ornare odio.</li>
        <li>- Morbi accumsan ipsum velit. Nam nec tellus a odio tincidunt auctor a ornare odio.</li>
        <li>- Morbi accumsan ipsum velit. Nam nec tellus a odio tincidunt auctor a ornare odio.</li>
        <li>- Morbi accumsan ipsum velit. Nam nec tellus a odio tincidunt auctor a ornare odio.</li>
      </ul>
    </div>
    <h2 class="services-title">PRODUCTS &amp; SERVICES</h2>
    <div class="service service--collab">
      <svg width="34" height="34" viewBox="0 0 34 34" aria-hidden="true">
        <g stroke="#1f4e8f" stroke-width="1.5"><line x1="17" y1="17" x2="5" y2="6"/><line x1="17" y1="17" x2="29" y2="6"/><line x1="17" y1="17" x2="4" y2="24"/><line x1="17" y1="17" x2="30" y2="24"/></g>
        <g fill="#e08a1e"><circle cx="5" cy="6" r="3"/><circle cx="29" cy="6" r="3"/><circle cx="4" cy="24" r="3"/><circle cx="30" cy="24" r="3"/></g>
        <circle cx="17" cy="12" r="4" fill="#1f4e8f"/><rect x="12" y="17" width="10" height="12" rx="3" fill="#1f4e8f"/>
      </svg>
      <h5>Collaboration &amp; Unified Communication Solutions</h5>
      <p>Morbi accumsan ipsum velit. Nam nec tellus a odio tincidunt auctor a ornare odio. Sed non mauris vitae erat consequat auctor eu in elit. Class aptent taciti sociosqu ad litora torquent per conubia nostra, per inceptos himenaeos.</p>
    </div>
    <div class="service service--infra">
      <svg width="34" height="34" viewBox="0 0 34 34" aria-hidden="true">
        <ellipse cx="17" cy="10" rx="13" ry="8" fill="#e08a1e"/>
        <rect x="9" y="14" width="16" height="5" fill="#1f4e8f"/><rect x="9" y="20" width="16" height="5" fill="#1f4e8f"/><rect x="9" y="26" width="16" height="5" fill="#1f4e8f"/>
      </svg>
      <h5>Infrastructure Solutions</h5>
      <p>Morbi accumsan ipsum velit. Nam nec tellus a odio tincidunt auctor a ornare odio. Sed non mauris vitae erat consequat auctor eu in elit. Class aptent taciti sociosqu ad litora torquent per conubia nostra, per inceptos himenaeos.</p>
    </div>
    <div class="partners" aria-label="Technology partners">
      <div class="partner"><svg width="40" height="14"><rect width="40" height="14" rx="3" fill="#c9ccd1"/></svg></div>
      <div class="partner"><svg width="26" height="30"><rect width="26" height="30" fill="#8d9a5e"/></svg></div>
      <div class="partner"><svg width="30" height="30"><circle cx="15" cy="15" r="12" fill="#9aa3ad"/></svg></div>
      <div class="partner"><svg width="30" height="24"><rect width="30" height="24" fill="#c8322d"/></svg></div>
      <div class="partner"><svg width="24" height="24"><circle cx="12" cy="12" r="10" fill="#2f6fb3"/></svg></div>
      <div class="partner"><svg width="40" height="14"><rect width="40" height="14" rx="3" fill="#1f4e8f"/></svg></div>
      <div class="partner"><svg width="40" height="10"><rect width="40" height="10" fill="#4a4f55"/></svg></div>
      <div class="partner"><svg width="40" height="14"><rect width="40" height="14" rx="3" fill="#2e8a4a"/></svg></div>
      <div class="partner partner--wide"><svg width="50" height="20"><rect width="50" height="20" fill="#3a6db0"/></svg></div>
      <div class="partner partner--wide"><svg width="60" height="20"><rect width="20" height="20" fill="#9aa3ad"/><rect x="26" y="6" width="34" height="8" fill="#9aa3ad"/></svg></div>
    </div>
    <div class="band-bottom"></div>
  </article>
</section>

<!-- Outside spread -->
<section class="spread spread--outside">
  <article class="page back">
    <div class="back__map" role="img" aria-label="Faint world map in lighter blue"></div>
    <div class="back__name"><span class="mark"></span>VELMOR INTEGRATED</div>
    <div class="back__sub">INTEGRATED SOLUTIONS</div>
    <div class="contact contact--eg">
      <h6>VELMOR TECHNOLOGIES, EGYPT</h6>
      <p><b>Address:</b> Office 12, Nile Tower, Cairo</p>
      <p><b>Tel:</b> +20 2 1234 5678</p>
      <p><b>E-mail:</b> info@velmorgroup.net</p>
      <p><b>Sales:</b> sales@velmorgroup.net</p>
      <p><b>Support:</b> support@velmorgroup.net</p>
    </div>
    <div class="contact contact--ksa">
      <h6>VELMOR TECHNOLOGIES, KSA</h6>
      <p><b>Address:</b> P.O. Box 1200, Riyadh, Saudi Arabia</p>
      <p><b>Tel:</b> +966 11 234 5678</p>
      <p><b>E-mail:</b> ksa@velmorgroup.net</p>
    </div>
    <div class="shops">
      <div class="shop">
        <div class="shop__name"><i></i>Nile Call Kit</div>
        <div class="shop__url">nilecallkit.com</div>
      </div>
      <div class="shop">
        <div class="shop__name"><i></i>Dune Link Gear</div>
        <div class="shop__url">dunelinkgear.com</div>
      </div>
    </div>
  </article>

  <article class="page front">
    <div class="front__photos">
      <div class="photo-servers" role="img" aria-label="Photo of a server room with racks"></div>
      <div class="photo-phone" role="img" aria-label="Photo of a conference speakerphone on a table"></div>
    </div>
    <div class="front__url">www.velmorgroup.net</div>
    <div class="front__brand">
      <div class="front__name"><i></i>VELMOR</div>
      <div class="front__tagline-sub">INTEGRATED SOLUTIONS</div>
    </div>
    <div class="front__claim">
      <div class="lead">The House of Unified</div>
      <div class="main">COMMUNICATION</div>
    </div>
  </article>
</section>

</body>
</html>
```